Hip surgeon needs a stationery design

I need a new stationery design for my private practice.
My practice is focused in hip arthroplasty (hip prosthesis).
I'd like to see designs most in blue or shades of blue.
I've uploaded my new logo to help with the task.
Also, I'm a member of some societies and I've uploaded their logos either, so I'd like to see them in some of the stationeries.
Itens list:
business card
letterhead A4
envelope
prescription block A5
one fold for A4 (please see the archive "pocket")
Personal data:
Dr. Renato L. Ferraz
CRM/PR 73915
site: www.clinicaarticular.com.br
email: dr.renato@clinicaarticular.com.br
Adress:
Rua Benedito Almeida Prates, 912
Campo Alegre - Curitiba/PR
41 35718206 I 35718207
Updates
I forgot to mention that my practice is focused primarily in hip arthroplasty (total hip prosthesis) and the target audience range from young adults to the elderly.
I also perform hip preserving surgeries (open and arthroscopic procedures) and pelvic and hip fracture surgery (trauma).
- Any "cleaner" fonts are welcome

```html
<!DOCTYPE html>
<html lang="pt">
<head>
<meta charset="utf-8">
<title>Dr. Renato L. Ferraz – Stationery</title>
<link rel="stylesheet" href="https://fonts.googleapis.com/css2?family=Roboto+Condensed:wght@400;700&family=Montserrat:wght@700&family=Open+Sans:wght@400&display=swap">
<style>
  :root {
    --stage: #8c8c8c;
    --paper: #ffffff;
    --blue: #1a7fc2;
    --cyan: #1fa6e0;
    --sub: #1f9ddb;
    --ink: #333333;
    --rule: #9a9a9a;
    --mark: #eeeeee;
    --label: #f2f2f2;
  }
  * { margin: 0; padding: 0; box-sizing: border-box; }
  html, body { width: 1200px; height: 640px; overflow: hidden; }
  body {
    background: var(--stage);
    position: relative;
    font-family: "Roboto Condensed", "Arial Narrow", sans-serif;
  }
  .sheet {
    position: absolute;
    background: var(--paper);
    overflow: hidden;
    box-shadow: 2px 2px 4px rgba(0,0,0,.35);
  }
  .bands { position: absolute; left: 0; bottom: 0; width: 100%; display: block; }
  .faint-disc {
    position: absolute;
    border-radius: 50%;
    background: var(--mark);
  }

  /* identity block */
  .identity { position: absolute; display: flex; align-items: center; }
  .identity .dot { border-radius: 50%; background: var(--blue); flex: none; }
  .identity .name { color: var(--blue); line-height: 1.05; }
  .identity .specialty { color: var(--sub); line-height: 1.1; }

  /* contact lists */
  .contacts { position: absolute; list-style: none; color: var(--ink); }
  .contacts li { display: flex; align-items: center; white-space: nowrap; }
  .contacts svg { flex: none; fill: var(--cyan); }

  /* letterhead */
  .letterhead { left: 22px; top: 38px; width: 452px; height: 580px; }
  .letterhead .top-rule { position: absolute; top: 0; left: 0; right: 0; height: 4px; background: var(--cyan); }
  .letterhead .identity { left: 30px; top: 30px; }
  .letterhead .dot { width: 42px; height: 42px; margin-right: 6px; }
  .letterhead .name { font-size: 19px; }
  .letterhead .specialty { font-size: 14px; }
  .letterhead .contacts {
    left: 334px; top: 30px; font-size: 5.5px; line-height: 8px;
    border-left: 1px solid var(--rule); padding-left: 6px;
  }
  .letterhead .contacts svg { width: 5px; height: 5px; margin-right: 3px; }
  .letterhead .faint-disc { left: 288px; top: 372px; width: 164px; height: 164px; }

  /* business card */
  .card-front { left: 513px; top: 37px; width: 275px; height: 161px; }
  .card-front .identity { left: 20px; top: 18px; }
  .card-front .dot { width: 34px; height: 34px; margin-right: 5px; }
  .card-front .name { font-size: 14.5px; }
  .card-front .specialty { font-size: 11px; }
  .card-front .holder { position: absolute; right: 14px; top: 62px; text-align: right; }
  .card-front .holder-name { font-family: "Montserrat", sans-serif; font-size: 10.5px; color: var(--blue); letter-spacing: .3px; }
  .card-front .holder-role { font-size: 6.5px; color: var(--ink); }
  .card-front .divider { position: absolute; left: 22px; right: 14px; top: 85px; height: 1px; background: var(--rule); }
  .card-front .contacts { left: 22px; top: 91px; font-size: 7px; line-height: 9.6px; }
  .card-front .contacts svg { width: 6px; height: 6px; margin-right: 4px; }

  .card-back { left: 806px; top: 37px; width: 276px; height: 161px; background: var(--blue); }
  .card-back .identity { left: 27px; top: 57px; }
  .card-back .dot { width: 46px; height: 46px; margin-right: 8px; background: var(--paper); }
  .card-back .name { font-size: 22px; color: var(--paper); }
  .card-back .specialty { font-size: 15.5px; color: var(--paper); }

  /* envelope */
  .envelope-front { left: 514px; top: 219px; width: 408px; height: 188px; }
  .envelope-front .identity { left: 28px; top: 23px; }
  .envelope-front .dot { width: 27px; height: 27px; margin-right: 4px; }
  .envelope-front .name { font-size: 12px; }
  .envelope-front .specialty { font-size: 9px; }
  .envelope-front .contacts {
    left: 60px; top: 54px; font-size: 5.5px; line-height: 8px;
    border-left: 1px solid var(--rule); padding-left: 5px;
  }
  .envelope-front .contacts svg { width: 5px; height: 5px; margin-right: 3px; }
  .envelope-front .faint-disc { left: 292px; top: 43px; width: 124px; height: 124px; }

  .envelope-back { left: 515px; top: 431px; width: 407px; height: 187px; }
  .envelope-back .flap { position: absolute; left: 0; top: 0; width: 100%; height: 60px; display: block; }
  .envelope-back .seal {
    position: absolute; left: 0; right: 0; top: 18px;
    display: flex; justify-content: center; align-items: center;
    color: var(--paper); font-size: 12px;
  }
  .envelope-back .seal .dot { width: 22px; height: 22px; border-radius: 50%; background: var(--paper); margin-right: 6px; }

  /* presentation labels */
  .sheet-list {
    position: absolute; left: 984px; top: 515px; list-style: none;
    font-family: "Open Sans", Arial, sans-serif; color: var(--label);
  }
  .sheet-list .heading { font-size: 17.5px; line-height: 22px; }
  .sheet-list li { font-size: 12.5px; line-height: 16.6px; }
</style>
</head>
<body>

<svg width="0" height="0" style="position:absolute" aria-hidden="true">
  <defs>
    <symbol id="i-phone" viewBox="0 0 10 10"><rect x="1" y="5" width="8" height="4" rx="1"/><path d="M0 4 Q5 0 10 4 L8 5 L2 5Z"/></symbol>
    <symbol id="i-mobile" viewBox="0 0 10 10"><rect x="2.5" y="0" width="5" height="10" rx="1"/><rect x="3.5" y="1.2" width="3" height="6" fill="#fff"/></symbol>
    <symbol id="i-mail" viewBox="0 0 10 10"><rect x="0" y="2" width="10" height="6.5" rx="1"/><path d="M0.5 2.5 L5 6 L9.5 2.5" stroke="#fff" fill="none" stroke-width="1"/></symbol>
    <symbol id="i-web" viewBox="0 0 10 10"><circle cx="5" cy="5" r="4.5"/><ellipse cx="5" cy="5" rx="1.8" ry="4.2" fill="none" stroke="#fff" stroke-width=".8"/><path d="M0.5 5 H9.5" stroke="#fff" stroke-width=".8"/></symbol>
    <symbol id="i-pin" viewBox="0 0 10 10"><path d="M5 10 L1.8 5.2 A3.7 3.7 0 1 1 8.2 5.2Z"/><circle cx="5" cy="3.6" r="1.4" fill="#fff"/></symbol>
  </defs>
</svg>

<!-- Letterhead -->
<section class="sheet letterhead" aria-label="Letterhead">
  <div class="top-rule"></div>
  <div class="identity">
    <span class="dot"></span>
    <div><div class="name">Dr. Renato L. Ferraz</div><div class="specialty">Cirurgia do Quadril</div></div>
  </div>
  <ul class="contacts">
    <li><svg><use href="#i-phone"/></svg>+0 412.635.7190</li>
    <li><svg><use href="#i-web"/></svg>www.clinicaarticular.com.br</li>
    <li><svg><use href="#i-mail"/></svg>dr.renato@clinicaarticular.com.br</li>
    <li><svg><use href="#i-pin"/></svg>Rua Benedito Almeida Prates, 912</li>
  </ul>
  <div class="faint-disc"></div>
  <svg class="bands" viewBox="0 0 452 20" height="20" aria-hidden="true">
    <rect x="0" y="10" width="266" height="10" fill="var(--cyan)"/>
    <path d="M270 20 L274 4 Q275 0 280 0 H452 V20Z" fill="var(--blue)"/>
  </svg>
</section>

<!-- Business card front -->
<section class="sheet card-front" aria-label="Business card front">
  <div class="identity">
    <span class="dot"></span>
    <div><div class="name">Dr. Renato L. Ferraz</div><div class="specialty">Cirurgia do Quadril</div></div>
  </div>
  <div class="holder">
    <div class="holder-name">Marcos Vidal</div>
    <div class="holder-role">Managing Director</div>
  </div>
  <div class="divider"></div>
  <ul class="contacts">
    <li><svg><use href="#i-mobile"/></svg>+0 412.635.7190</li>
    <li><svg><use href="#i-phone"/></svg>+0 412.635.7190</li>
    <li><svg><use href="#i-mail"/></svg>dr.renato@clinicaarticular.com.br</li>
    <li><svg><use href="#i-web"/></svg>www.clinicaarticular.com.br</li>
    <li><svg><use href="#i-pin"/></svg>Rua Benedito Almeida Prates, 912</li>
  </ul>
  <svg class="bands" viewBox="0 0 275 16" height="16" aria-hidden="true">
    <rect x="0" y="5" width="160" height="11" fill="var(--cyan)"/>
    <path d="M163 16 L167 3 Q168 0 172 0 H275 V16Z" fill="var(--blue)"/>
  </svg>
</section>

<!-- Business card back -->
<section class="sheet card-back" aria-label="Business card back">
  <div class="identity">
    <span class="dot"></span>
    <div><div class="name">Dr. Renato L. Ferraz</div><div class="specialty">Cirurgia do Quadril</div></div>
  </div>
</section>

<!-- Envelope front -->
<section class="sheet envelope-front" aria-label="Envelope front">
  <div class="identity">
    <span class="dot"></span>
    <div><div class="name">Dr. Renato L. Ferraz</div><div class="specialty">Cirurgia do Quadril</div></div>
  </div>
  <ul class="contacts">
    <li><svg><use href="#i-web"/></svg>www.clinicaarticular.com.br</li>
    <li><svg><use href="#i-pin"/></svg>Rua Benedito Almeida Prates, 912</li>
  </ul>
  <div class="faint-disc"></div>
  <svg class="bands" viewBox="0 0 408 19" height="19" aria-hidden="true">
    <rect x="0" y="8" width="238" height="11" fill="var(--cyan)"/>
    <path d="M241 19 L245 4 Q246 0 251 0 H408 V19Z" fill="var(--blue)"/>
  </svg>
</section>

<!-- Envelope back -->
<section class="sheet envelope-back" aria-label="Envelope back">
  <svg class="flap" viewBox="0 0 407 60" preserveAspectRatio="none" aria-hidden="true">
    <path d="M0 0 H407 V30 Q407 40 402 46 Q398 58 384 58 H23 Q9 58 5 46 Q0 40 0 30Z" fill="var(--blue)"/>
  </svg>
  <div class="seal"><span class="dot"></span>Dr. Renato L. Ferraz</div>
</section>

<ul class="sheet-list">
  <li class="heading">Stationery Design</li>
  <li>Business Card front</li>
  <li>Business Card Back</li>
  <li>Letterhead</li>
  <li>Envelope Front</li>
  <li>Envelope Back</li>
</ul>

</body>
</html>
```